Financial Consulting Company in need of technical diagram

Attached is a basic template to follow, however the following changes must be made:
- Get rid of reflection boxes at the bottom
-Delete anything in parentheses
-Change top box to read "Uncover Value Opportunities"
-Change bottom right box to read "Sales and Operations Planning"
-Change bottom left box to read "Financial Planning"

Additionally we would like to see something a little more creative and cohesive. One possibility is using "Cheveron" type arrows to show the "wheel" effect.

Please email tmorven@brightlake7.example if you have any questions!
Updates

Please see newly uploaded image for an example of how we would like it re-created.

Industry/Entity Type

Financial

Requirements
Must have
• I'm looking for something that keeps the "wheel" approach, but is not a direct re-creation of the example given. The boxes for example, dont' necessarily need to stay boxes. Feel free to play around with placement as well.
Nice to have
• Please see green wheel for example of how it can be re-created.

```html
<!DOCTYPE html>
<html lang="en">
<head>
<meta charset="utf-8">
<title>Value Planning Wheel</title>
<link href="https://fonts.googleapis.com/css2?family=Montserrat:wght@600&display=swap" rel="stylesheet">
<style>
  :root {
    --canvas-bg: #ffffff;
    --chevron-grey: #9b9b9b;
    --stage-gold: #c9a352;
    --label-white: #ffffff;
  }
  html, body {
    margin: 0;
    padding: 0;
    overflow: hidden;
    background: var(--canvas-bg);
  }
  .wheel-canvas {
    position: relative;
    width: 1200px;
    height: 900px;
    overflow: hidden;
    background: var(--canvas-bg);
  }
  .wheel-graphic {
    position: absolute;
    inset: 0;
  }
  .chevron-segment {
    fill: var(--chevron-grey);
    filter: drop-shadow(1px 2px 2px rgba(0,0,0,0.35));
  }
  .stage-disc {
    fill: var(--stage-gold);
  }
  .stage-label {
    position: absolute;
    width: 150px;
    transform: translate(-50%, -50%);
    margin: 0;
    font-family: "Montserrat", Arial, sans-serif;
    font-weight: 600;
    font-size: 17px;
    line-height: 19.5px;
    letter-spacing: 0.6px;
    color: var(--label-white);
    text-align: center;
  }
</style>
</head>
<body>
<main class="wheel-canvas">
  <svg class="wheel-graphic" width="1200" height="900" viewBox="0 0 1200 900" aria-hidden="true">
    <g class="chevron-ring">
      <path class="chevron-segment" d="M435.7 215.1 A310 310 0 0 1 745.5 204.3 L763.5 244.5 L722.1 248.4 A260 260 0 0 0 462.2 257.5 L479.6 219.7 Z"/>
      <path class="chevron-segment" transform="rotate(72 600 478)" d="M435.7 215.1 A310 310 0 0 1 745.5 204.3 L763.5 244.5 L722.1 248.4 A260 260 0 0 0 462.2 257.5 L479.6 219.7 Z"/>
      <path class="chevron-segment" transform="rotate(144 600 478)" d="M435.7 215.1 A310 310 0 0 1 745.5 204.3 L763.5 244.5 L722.1 248.4 A260 260 0 0 0 462.2 257.5 L479.6 219.7 Z"/>
      <path class="chevron-segment" transform="rotate(216 600 478)" d="M435.7 215.1 A310 310 0 0 1 745.5 204.3 L763.5 244.5 L722.1 248.4 A260 260 0 0 0 462.2 257.5 L479.6 219.7 Z"/>
      <path class="chevron-segment" transform="rotate(288 600 478)" d="M435.7 215.1 A310 310 0 0 1 745.5 204.3 L763.5 244.5 L722.1 248.4 A260 260 0 0 0 462.2 257.5 L479.6 219.7 Z"/>
    </g>
    <g class="stage-discs">
      <circle class="stage-disc" cx="600" cy="193" r="88"/>
      <circle class="stage-disc" cx="866" cy="385" r="88"/>
      <circle class="stage-disc" cx="764" cy="695" r="88"/>
      <circle class="stage-disc" cx="437" cy="695" r="88"/>
      <circle class="stage-disc" cx="336" cy="385" r="88"/>
    </g>
  </svg>

  <p class="stage-label" style="left:600px; top:191px;">Uncover<br>Value<br>Opportunities</p>
  <p class="stage-label" style="left:864px; top:383px;">Strategize<br>and Align</p>
  <p class="stage-label" style="left:763px; top:692px;">Sales and<br>Operations<br>Planning</p>
  <p class="stage-label" style="left:437px; top:692px;">Financial<br>Planning</p>
  <p class="stage-label" style="left:337px; top:383px;">Assess the<br>Results</p>
</main>
</body>
</html>
```